Webdesign für Kanal Vertrieb
Zielgruppe
Die lotte & brandt Media Marketing GmbH beschäftigt sich mit der Entwicklung, Vermarktung und dem Vertrieb von Medialeistungen aus den Bereichen Print, TV, Radio, Internet (Digital) und Events. Weiterhin erstellt das Unternehmen Kommunikation- und Marketingkonzepte sowie die komplette Realisierung von Events und TV-Produktionen. Im Weiteren werden auch branchenverwandten Anwendungen und Bereiche abgedeckt, die den Unternehmenszielen dienen. Das Unternehmen betreut, vermittelt und vermarktet im weiteren Prominente, Kunstler und Moderatoren.
Die Zielgruppe ist B2B
Unsere Seite ist aktuell nun 2 Jahre alt und wir benötigen ein frisches Re-Design
Das Design soll zum Style des Logos passen, es soll elegant und professionelle hervorgehoben werden.
Die jetzige Seite findet mal unter www.lotte-brandt.de
Aufgabenstellung
Das Design soll frisch und elegant wirken, sowie einen professionellen Eindruck für eine Media Agentur machen. Das ganze soll dann im Anschluss in Word Press integrier bar sein und auch dort gepflegt werden.

```html
<!DOCTYPE html>
<html lang="de">
<head>
<meta charset="utf-8">
<title>lotte &amp; brandt – Kanal Vertrieb</title>
<link href="https://fonts.googleapis.com/css2?family=Poppins:wght@300;400;500;600&display=swap" rel="stylesheet">
<style>
:root{
  --bg:#0d0d0d;
  --panel:#161616;
  --red:#e0241f;
  --red-dark:#9a1a18;
  --white:#ffffff;
  --muted:#9a9a9a;
}
*{margin:0;padding:0;box-sizing:border-box}
html,body{width:1200px;height:3263px;overflow:hidden;background:var(--bg);color:var(--white);font-family:'Poppins',sans-serif}
.page{position:relative;width:1200px;height:3263px}
.abs{position:absolute}
.link{color:var(--red);font-size:11px;display:flex;align-items:center;gap:10px;text-decoration:none}
.link svg{width:16px;height:8px}
.copy{color:var(--muted);font-size:10px;line-height:17.5px;font-weight:300}
.logo{font-size:26px;font-weight:300;letter-spacing:1px;line-height:1}
.logo small{display:block;font-size:7px;letter-spacing:5px;margin-top:6px;text-transform:uppercase;text-align:center}

/* hero */
.hero{left:0;top:0;width:1200px;height:587px;background:var(--bg)}
.hero-photo{left:0;top:0;width:690px;height:587px;background:linear-gradient(120deg,#cfcfcf 0%,#6b6b6b 30%,#2a2a2a 60%,#0f0f0f 100%)}
.menu{left:1035px;top:50px;font-size:12px;font-weight:500;display:flex;align-items:center;gap:12px}
.hero-title{left:780px;top:230px;width:300px;font-size:24px;font-weight:500;line-height:31px;letter-spacing:.5px}

/* services */
.services{left:0;top:587px;width:1200px;height:414px;background:var(--panel)}
.section-title{font-size:30px;font-weight:600;line-height:40px}
.service{width:230px}
.badge{width:30px;height:30px;position:relative;margin-bottom:14px}
.badge::before{content:"";position:absolute;left:0;top:0;width:30px;height:30px;border-radius:3px;background:var(--red)}
.badge span{position:absolute;left:3px;top:0;width:27px;height:26px;background:#0e0e0e;border-radius:3px;font-size:10px;display:flex;align-items:center;justify-content:center}
.service h3{font-size:20px;font-weight:400;margin-bottom:10px}

/* projects */
.proj{overflow:hidden}
.proj-title{font-size:21px;font-weight:600;line-height:23px}
.btn{background:var(--white);color:var(--red);border-radius:16px;font-size:11px;display:inline-flex;align-items:center;justify-content:center}

/* testimonial */
.quote-box{left:100px;top:1659px;width:1000px;height:316px;background:var(--panel)}
.quote{left:525px;top:1720px;width:460px;font-size:20px;line-height:30px;font-weight:400}
.arrow-btn{width:28px;height:28px;border-radius:50%;display:flex;align-items:center;justify-content:center}

/* jobs */
.job{top:2256px;height:197px;background:var(--panel);padding:28px 29px}
.job h3{font-size:16px;font-weight:400;margin:14px 0 12px}

/* cta */
.cta{left:99px;top:2572px;width:1001px;height:317px;background:var(--red)}
.cta-photo{left:748px;top:2528px;width:316px;height:361px;background:linear-gradient(180deg,#d9c0b0 0%,#9bb7d8 55%,#7fa3cf 100%);border-radius:140px 140px 0 0}

/* footer */
.footer{left:0;top:3007px;width:1200px;height:256px;background:var(--panel)}
.fcol h4{font-size:11px;font-weight:500;margin-bottom:10px}
.fcol p{font-size:10px;color:#c8c8c8;line-height:17.5px;font-weight:300;display:flex;align-items:center;gap:5px}
</style>
</head>
<body>
<div class="page">

  <!-- hero -->
  <section class="abs hero"></section>
  <div class="abs hero-photo" role="img" aria-label="Schwarzweißfoto eines Kameramanns am Filmset"></div>
  <div class="abs logo" style="left:100px;top:40px">lotte &amp; brandt<small>Kanal Vertrieb</small></div>
  <div class="abs menu">Menü
    <svg width="18" height="10" viewBox="0 0 18 10"><path d="M0 1h18M4 5h14M0 9h18" stroke="#fff" stroke-width="1.3"/></svg>
  </div>
  <h1 class="abs hero-title">Erzählen Sie uns Ihre<br>Geschichte, wir<br>erzählen sie weiter.</h1>
  <a class="abs link" style="left:780px;top:339px">Unsere Geschichten <svg viewBox="0 0 16 8"><path d="M0 4h15M11 1l4 3-4 3" stroke="#e0241f" fill="none"/></svg></a>

  <!-- services -->
  <section class="abs services"></section>
  <h2 class="abs section-title" style="left:100px;top:652px">Was wir machen</h2>
  <p class="abs copy" style="left:100px;top:704px;width:300px">Weit hinten, hinter den Wortbergen, fern der Länder Vokalien und Konsonantien leben die Blindtexte. Abgeschieden wohnen sie in Buchstabhausen an der Küste des Semantik, eines großen Sprachozeans.</p>
  <a class="abs link" style="left:100px;top:788px">Nehmen Sie Kontakt auf <svg viewBox="0 0 16 8"><path d="M0 4h15M11 1l4 3-4 3" stroke="#e0241f" fill="none"/></svg></a>

  <div class="abs service" style="left:525px;top:655px"><div class="badge"><span>01</span></div><h3>Internet</h3><p class="copy">Weit hinten, hinter den Wortbergen, fern der Länder Vokalien und Konsonantien leben die Blindtexte.</p></div>
  <div class="abs service" style="left:780px;top:655px"><div class="badge"><span>02</span></div><h3>Events</h3><p class="copy">Weit hinten, hinter den Wortbergen, fern der Länder Vokalien und Konsonantien leben die Blindtexte.</p></div>
  <div class="abs service" style="left:525px;top:810px"><div class="badge"><span>03</span></div><h3>TV Produktionen</h3><p class="copy">Weit hinten, hinter den Wortbergen, fern der Länder Vokalien und Konsonantien leben die Blindtexte.</p></div>
  <div class="abs service" style="left:780px;top:810px"><div class="badge"><span>04</span></div><h3>Print</h3><p class="copy">Weit hinten, hinter den Wortbergen, fern der Länder Vokalien und Konsonantien leben die Blindtexte.</p></div>

  <!-- projects -->
  <h2 class="abs section-title" style="left:100px;top:1082px">Unsere Projekte</h2>
  <a class="abs link" style="left:1013px;top:1098px;font-size:10px">Alle Projekte <svg viewBox="0 0 16 8"><path d="M0 4h15M11 1l4 3-4 3" stroke="#e0241f" fill="none"/></svg></a>

  <div class="abs proj" style="left:100px;top:1163px;width:575px;height:375px">
    <div class="abs" role="img" aria-label="Kamera bei einem Dreh, rot eingefärbt" style="left:0;top:0;width:320px;height:375px;background:linear-gradient(160deg,#c9302c,#e0403a 60%,#e55049)"></div>
    <div class="abs" role="img" aria-label="Interview mit zwei Köchen auf einem Event" style="left:320px;top:0;width:255px;height:375px;background:linear-gradient(180deg,#7d7a72,#5a5853 50%,#8e8b85)"></div>
    <div class="abs proj-title" style="left:36px;top:255px">Mit Sonnenwelt TV<br>auf Mallorca</div>
    <span class="abs btn" style="left:37px;top:311px;width:115px;height:29px">Zum Projekt</span>
  </div>

  <div class="abs proj" style="left:694px;top:1163px;width:406px;height:177px">
    <div class="abs" role="img" aria-label="Zwei Personen an einem Messestand" style="left:0;top:0;width:137px;height:177px;background:linear-gradient(180deg,#e8e8ea,#b7b9c0)"></div>
    <div class="abs" style="left:137px;top:0;width:269px;height:177px;background:linear-gradient(135deg,#d9534f,#e0241f)"></div>
    <div class="abs proj-title" style="left:162px;top:106px">#weCare Europa</div>
    <a class="abs link" style="left:162px;top:141px;color:#fff">Zum Projekt <svg viewBox="0 0 16 8"><path d="M0 4h15M11 1l4 3-4 3" stroke="#fff" fill="none"/></svg></a>
  </div>

  <div class="abs proj" style="left:694px;top:1361px;width:406px;height:177px">
    <div class="abs" role="img" aria-label="Titelseiten mehrerer Fernsehzeitschriften" style="left:0;top:0;width:137px;height:177px;background:linear-gradient(135deg,#a9cdef,#d94a3a 60%,#f0c24b)"></div>
    <div class="abs" style="left:137px;top:0;width:269px;height:177px;background:linear-gradient(135deg,#e0403a,#c42a3a)"></div>
    <div class="abs proj-title" style="left:162px;top:106px">Unser Fernsehheft</div>
    <a class="abs link" style="left:162px;top:141px;color:#fff">Zum Projekt <svg viewBox="0 0 16 8"><path d="M0 4h15M11 1l4 3-4 3" stroke="#fff" fill="none"/></svg></a>
  </div>

  <!-- testimonial -->
  <div class="abs quote-box"></div>
  <h2 class="abs" style="left:150px;top:1762px;font-size:24px;font-weight:500;line-height:30px">Das sagen<br>unsere Kunden</h2>
  <p class="abs copy" style="left:150px;top:1836px;width:270px">Weit hinten, hinter den Wortbergen, fern der Länder Vokalien und Konsonantien leben die Blindtexte.</p>
  <p class="abs quote">"Die beste Agentur, mit der wir bisher zusammengearbeitet haben. Sie verstehen unser Produkt und sind in der Lage, neue Funktionen mit einem großen Fokus hinzuzufügen."</p>
  <div class="abs" role="img" aria-label="Porträt der Kundin" style="left:525px;top:1877px;width:32px;height:32px;border-radius:50%;background:linear-gradient(135deg,#d8b59c,#7a5a48)"></div>
  <div class="abs" style="left:569px;top:1882px;font-size:11px;font-weight:500;line-height:14px">Marie Beispiel<br><span style="font-size:7px;font-weight:400;color:#ccc">Sonnenwelt TV</span></div>
  <div class="abs arrow-btn" style="left:993px;top:1920px;background:var(--red-dark)"><svg width="8" height="12"><path d="M6 1L2 6l4 5" stroke="#fff" stroke-width="2" fill="none"/></svg></div>
  <div class="abs arrow-btn" style="left:1030px;top:1920px;background:var(--red)"><svg width="8" height="12"><path d="M2 1l4 5-4 5" stroke="#fff" stroke-width="2" fill="none"/></svg></div>

  <!-- team -->
  <h2 class="abs" style="left:100px;top:2066px;font-size:32px;font-weight:600;line-height:42px">Werde ein Teil des<br>großartigen Teams</h2>
  <p class="abs copy" style="left:100px;top:2162px;width:500px">Das weiße Blatt Papier? Hab keine Angst. Denn hätte, könnte, würde geben wir keine Chance. Wir sind Profis und setzen unsere Ideen um. Und wenn jemand in der Sackgasse durchhängt, holen wir ihn wieder raus. Mit Methoden, Teamspirit und richtig gutem Kaffee</p>

  <div class="abs job" style="left:100px;width:319px">
    <svg width="20" height="20" viewBox="0 0 20 20"><path d="M3 3l14 14M17 3L3 17" stroke="#e0241f" stroke-width="3"/></svg>
    <h3>Mediengestalter (m/w/x)</h3>
    <p class="copy">Weit hinten, hinter den Wortbergen, fern der Länder Vokalien und Konsonantien leben die Blindtexte.</p>
    <a class="link" style="margin-top:8px">Jetzt bewerben <svg viewBox="0 0 16 8"><path d="M0 4h15M11 1l4 3-4 3" stroke="#e0241f" fill="none"/></svg></a>
  </div>
  <div class="abs job" style="left:440px;width:320px">
    <svg width="20" height="20" viewBox="0 0 20 20"><rect x="3" y="2" width="12" height="16" rx="1" fill="#e0241f"/><path d="M6 7h6M6 11h6" stroke="#161616" stroke-width="1.5"/></svg>
    <h3>Projektmanager (m/w/x)</h3>
    <p class="copy">Weit hinten, hinter den Wortbergen, fern der Länder Vokalien und Konsonantien leben die Blindtexte.</p>
    <a class="link" style="margin-top:8px">Jetzt bewerben <svg viewBox="0 0 16 8"><path d="M0 4h15M11 1l4 3-4 3" stroke="#e0241f" fill="none"/></svg></a>
  </div>
  <div class="abs job" style="left:779px;width:321px">
    <svg width="22" height="20" viewBox="0 0 22 20"><circle cx="11" cy="5" r="3.5" fill="#e0241f"/><circle cx="4" cy="7" r="2.5" fill="#e0241f"/><circle cx="18" cy="7" r="2.5" fill="#e0241f"/><rect x="6" y="10" width="10" height="8" rx="2" fill="#e0241f"/></svg>
    <h3>Office Manager (m/w/x)</h3>
    <p class="copy">Weit hinten, hinter den Wortbergen, fern der Länder Vokalien und Konsonantien leben die Blindtexte.</p>
    <a class="link" style="margin-top:8px">Jetzt bewerben <svg viewBox="0 0 16 8"><path d="M0 4h15M11 1l4 3-4 3" stroke="#e0241f" fill="none"/></svg></a>
  </div>

  <!-- call to action -->
  <div class="abs cta"></div>
  <div class="abs cta-photo" role="img" aria-label="Porträt des Geschäftsführers im hellblauen Sakko"></div>
  <h2 class="abs" style="left:165px;top:2636px;font-size:30px;font-weight:600;line-height:38px">Starten Sie jetzt Ihr<br>Projekt mit uns!</h2>
  <p class="abs" style="left:165px;top:2720px;width:490px;font-size:10px;line-height:17.5px;font-weight:300">Wo gibt's denn sowas? In Essen! Im Herzen des Ruhrgebiets!<br>Da, wo man nicht „drum herum redet"! Treten Sie mit uns in Kontakt und fordern Sie uns heraus! Schildern Sie einfach Ihre Wünsche und erhalten Sie umgehend Mediaanalysen und konkrete Vorschläge und Angebote.</p>
  <span class="abs btn" style="left:165px;top:2800px;width:174px;height:39px">Zum Kontaktformular</span>

  <!-- footer -->
  <footer class="abs footer"></footer>
  <div class="abs logo" style="left:100px;top:3060px;font-size:24px">lotte &amp; brandt<small>Kanal Vertrieb</small></div>
  <p class="abs" style="left:100px;top:3113px;font-size:10px;line-height:17.5px;font-weight:300">Wo gibt's denn sowas?<br>In Essen! Im Herzen des Ruhrgebiets!<br>Da, wo man nicht „drum herum redet"!</p>

  <div class="abs fcol" style="left:440px;top:3061px"><h4>Kompetenzen</h4><p>Internet</p><p>Events</p><p>TV Produktionen</p><p>Print</p></div>
  <div class="abs fcol" style="left:609px;top:3061px"><h4>Über uns</h4><p>Agentur</p><p>Jobs</p><p>Kontakt</p></div>
  <div class="abs fcol" style="left:779px;top:3061px"><h4>Kontakt</h4><p>Kontaktformular</p><p>Anfahrt</p><p>Newsletter</p></div>
  <div class="abs fcol" style="left:949px;top:3061px"><h4>lotte &amp; brandt</h4>
    <p><svg width="8" height="8" viewBox="0 0 8 8"><path d="M1 1c0 4 2 6 6 6l0-2-2-.5-1 1C3 5 3 5 2.5 4l1-1L3 1z" fill="#ccc"/></svg>0171 987 6543</p>
    <p><svg width="8" height="7" viewBox="0 0 8 7"><rect x="0" y="0.5" width="8" height="6" fill="#ccc"/><path d="M0 1l4 3 4-3" stroke="#161616" fill="none"/></svg>info@lottebrandt.de</p>
  </div>

  <p class="abs" style="left:100px;top:3229px;font-size:10px;font-weight:500">Impressum | Datenschutz | AGB</p>
  <p class="abs" style="left:934px;top:3229px;font-size:10px;font-weight:500">Folgen Sie uns auf</p>
  <div class="abs" style="left:1039px;top:3228px;width:12px;height:12px;border-radius:50%;background:#fff"></div>
  <div class="abs" style="left:1060px;top:3228px;width:12px;height:12px;background:#fff"></div>
  <div class="abs" style="left:1081px;top:3228px;width:18px;height:12px;border-radius:3px;background:#fff"></div>

</div>
</body>
</html>
```